Copperfield Wire - Subscription Landing page

we need responsive landing page for a new news service about the Blockchain innovations coins and startups, the landing page includes vertical video player and call to action button, attach mockup.
temporary page
http://www.cpfw.io/
1 page

```html
<!DOCTYPE html>
<html lang="en">
<head>
<meta charset="utf-8">
<title>Copperfield Wire – Be Ready For Tomorrow</title>
<link href="https://fonts.googleapis.com/css2?family=Lato:wght@300;400;700;900&display=swap" rel="stylesheet">
<style>
:root{
  --brand-red:#e21f26;
  --band-red:#c1111b;
  --navy:#141f6b;
  --navy-deep:#0b1240;
  --teal:#35d6b3;
  --panel:rgba(6,8,22,.86);
  --white:#ffffff;
  --text-soft:#e6e8f2;
  --phone-frame:#f4f4f4;
  --phone-edge:#b9bcc2;
}
*{box-sizing:border-box;margin:0;padding:0}
html,body{width:1200px;height:842px;overflow:hidden;background:var(--white);font-family:"Lato",Arial,sans-serif}
.page{position:relative;width:1200px;height:842px;overflow:hidden}
.site-header{position:absolute;top:0;left:0;width:1200px;height:110px;display:flex;align-items:center;justify-content:center;gap:10px}
.brand-dot{width:34px;height:34px;border-radius:50%;background:var(--brand-red)}
.brand-name{font-weight:900;font-size:28px;color:var(--brand-red);letter-spacing:.3px}
.hero{position:absolute;top:110px;left:0;width:1200px;height:620px;
  background:
   radial-gradient(circle at 1158px 290px,rgba(53,214,179,.75) 0,rgba(53,214,179,.15) 40px,transparent 90px),
   radial-gradient(ellipse 140px 60px at 900px 60px,rgba(53,214,179,.25),transparent),
   radial-gradient(ellipse 260px 200px at 1020px 420px,rgba(40,150,150,.35),transparent),
   radial-gradient(ellipse 200px 120px at 880px 600px,rgba(53,214,179,.3),transparent),
   linear-gradient(100deg,var(--navy) 0%,#111a5c 55%,var(--navy-deep) 100%)}
.hero-red{position:absolute;top:0;left:0;width:326px;height:620px;background:var(--band-red)}
.decor-area{position:absolute;left:446px;top:170px;width:360px;height:490px;
  background:radial-gradient(ellipse 180px 245px at 50% 50%,rgba(90,110,220,.16),transparent 75%)}
.promo{position:absolute;left:513px;top:290px;width:507px;height:332px;background:var(--panel);padding:52px 0 0 28px;color:var(--white)}
.promo-title{font-weight:900;font-size:25px;letter-spacing:3.4px;text-transform:uppercase}
.promo-text{margin-top:19px;width:462px;font-size:16.5px;line-height:27px;letter-spacing:.5px;color:var(--text-soft)}
.promo-sub{margin-top:26px;font-weight:300;font-size:16.5px;letter-spacing:.3px;color:var(--text-soft)}
.cta{display:inline-flex;align-items:center;justify-content:center;margin-top:22px;width:256px;height:44px;border-radius:22px;background:var(--band-red);color:var(--white);font-size:13.5px;letter-spacing:2.2px;text-transform:uppercase;text-decoration:none}
.phone{position:absolute;left:178px;top:227px;width:268px;height:517px;border-radius:34px;background:var(--phone-frame);border:2px solid var(--phone-edge);box-shadow:0 2px 8px rgba(0,0,0,.25)}
.phone-speaker{position:absolute;left:106px;top:18px;width:54px;height:5px;border-radius:3px;background:#8a8d93}
.phone-cam{position:absolute;top:16px;border-radius:50%;background:#222}
.phone-home{position:absolute;left:106px;top:481px;width:54px;height:16px;border-radius:8px;border:1.5px solid #9a9da3;background:#e9e9ea}
.video{position:absolute;left:14px;top:43px;width:237px;height:424px;overflow:hidden;
  background:linear-gradient(180deg,#8a90a8 0%,#c79aa5 30%,#d8c1b4 55%,#efe3dc 80%,#c9b7b3 100%)}
.video-bar{position:absolute;left:0;top:0;width:100%;height:58px;background:linear-gradient(180deg,rgba(0,0,0,.55),transparent);display:flex;align-items:center;gap:7px;padding:12px 0 0 10px}
.video-dot{width:24px;height:24px;border-radius:50%;background:var(--brand-red)}
.video-title{font-size:14px;color:var(--white);white-space:nowrap}
.video-url{position:absolute;right:10px;top:5px;font-size:9px;line-height:12px;color:var(--white);background:rgba(193,17,27,.85);padding:0 4px}
.video-play{position:absolute;left:92px;top:192px;width:58px;height:40px;border-radius:10px;background:rgba(30,30,30,.8);display:flex;align-items:center;justify-content:center}
.social{position:absolute;top:767px;left:0;width:1200px;display:flex;justify-content:center;gap:9px}
.social-item{width:44px;height:44px;border-radius:50%;display:flex;align-items:center;justify-content:center;color:var(--white);font-size:7.5px;font-weight:700;letter-spacing:.1px}
.s-page{background:#3b5998}.s-chirp{background:#1da1f2}.s-vid{background:#e62117}.s-photo{background:#b1368e}.s-wire{background:#2aa3dc}
</style>
</head>
<body>
<div class="page">
  <header class="site-header">
    <span class="brand-dot"></span>
    <span class="brand-name">Copperfield Wire</span>
  </header>

  <section class="hero">
    <div class="hero-red"></div>
  </section>

  <div class="decor-area" role="img" aria-label="Decorative pattern of coloured hexagons and circuit lines"></div>

  <div class="promo">
    <h1 class="promo-title">Be ready for tomorrow</h1>
    <p class="promo-text">Stay updated with all the latest blockchain innovations coins and startups in a daily video story.</p>
    <p class="promo-sub">Subscribe for free in one of our channels below:</p>
    <a class="cta" href="#">Browser notification</a>
  </div>

  <div class="phone">
    <span class="phone-speaker"></span>
    <span class="phone-cam" style="left:175px;top:18px;width:6px;height:6px"></span>
    <span class="phone-cam" style="left:195px;width:11px;height:11px"></span>
    <div class="video" role="img" aria-label="Vertical video preview: presenter in front of a city skyline at dusk">
      <span class="video-url">www.cpfw.io</span>
      <div class="video-bar"><span class="video-dot"></span><span class="video-title">Copperfield Wire - Soon</span></div>
      <span class="video-play"><svg width="16" height="18" viewBox="0 0 16 18"><polygon points="0,0 16,9 0,18" fill="#fff"/></svg></span>
    </div>
    <span class="phone-home"></span>
  </div>

  <nav class="social">
    <a class="social-item s-page">Pagebook</a>
    <a class="social-item s-chirp">Chirper</a>
    <a class="social-item s-vid">Vidstream</a>
    <a class="social-item s-photo">Photogrid</a>
    <a class="social-item s-wire">Wiregram</a>
  </nav>
</div>
</body>
</html>
```